Silverwell Tisane House needs a website with shopping cart

We are a herbal tea business that hand blends organic tea recipes for medicinal purposes and for customer enjoyment. We require a website that represents our elegant brand and our connection to plant medicine. We will require a home page, a products page, a contact us page with form and an information page. We will need to be able to photograph our teas and upload the images to the products page along with changing pricing and shipping costs, and the ability to add/change information and images to our information page as this page will be mostly about the different herbs we will use in the teas. Our teas will be 'loose leaf' (not in tea bags) and will be sold in glass jars. At this stage we only intend to use Quorvex as a method of payment for overseas customers and direct credit for New Zealand customers.

Target Market(s)

Tea drinkers, women, people interested in health/herbs, people looking for gifts

Industry/Entity Type

Shopping

Logo Text

Silverwell Tisane House

Coding

Coded - Design and coding required

Number of Pages Required

4 page

Font styles to use
Decorative

Requirements
Must have
• I am a herbalist and love plants, flowers and nature so would like the overall website and logo to represent this. I have attached the logo I had designed several years ago for myself as inspiration - the graduated greens are great and very vibrant which I like (sorry about the quality, I couldn't find the source files - NEW SOURCE FILE ADDED 23/04/15). This is an upmarket, niche product which is elegant and healthy.

```html
<!DOCTYPE html>
<html lang="en">
<head>
<meta charset="utf-8">
<title>Silverwell Tisane House</title>
<link href="https://fonts.googleapis.com/css2?family=Source+Sans+3:wght@400;600;700&display=swap" rel="stylesheet">
<style>
:root{
  --green:#2d8a35;
  --green-dark:#256f2b;
  --charcoal:#4a4a4a;
  --ink:#333;
  --muted:#555;
  --panel:#f2f2f2;
  --card-info:#efefef;
  --orange:#f08a1c;
  --white:#fff;
}
*{box-sizing:border-box;margin:0;padding:0}
html,body{width:714px;height:1200px;overflow:hidden;background:var(--white)}
body{position:relative;font-family:"Source Sans 3",sans-serif;color:var(--ink)}
.abs{position:absolute}
.top-rule{left:0;top:0;width:714px;height:2px;background:var(--green)}
.brand{left:58px;top:10px;width:120px}
.brand-mark{width:42px;height:42px;border-radius:50%;background:var(--green);margin-left:30px}
.brand-name{font-size:11px;font-weight:700;color:var(--ink);margin-top:6px;white-space:nowrap}
.brand-tag{font-size:4.5px;color:var(--green);letter-spacing:.2px;white-space:nowrap}
.utility{left:443px;top:29px;font-size:7.5px;color:var(--muted)}
.utility span{margin:0 5px}
.utility-divider{left:569px;top:24px;width:1px;height:20px;background:#ccc}
.cart{left:583px;top:28px;font-size:8.5px;color:var(--muted);display:flex;align-items:center;gap:5px}
.nav{top:60px;left:318px;display:flex;font-size:8.5px;font-weight:600;color:var(--ink)}
.nav a{color:inherit;text-decoration:none;display:block;height:16px;line-height:16px}
.nav .active{background:var(--green);color:var(--white);padding:0 10px;border-radius:2px}
.hero{left:0;top:84px;width:714px;height:319px;background:radial-gradient(ellipse at 45% 45%,#f3cf3a 0%,#e7d47a 25%,#d7dba0 45%,#c3cf7a 70%,#a9b95a 100%)}
.hero-arrow{width:22px;height:22px;border-radius:50%;background:rgba(120,120,120,.35);top:232px}
.hero-caption{left:58px;top:326px;width:406px;height:30px;background:rgba(45,138,53,.85);color:var(--white);font-size:10.5px;font-weight:600;line-height:30px;padding-left:9px}
.welcome-title{left:0;top:422px;width:714px;text-align:center;font-size:18px;font-weight:600;color:var(--ink)}
.welcome-text{left:60px;top:453px;width:594px;text-align:center;font-size:7.6px;line-height:11.6px;color:var(--ink)}
.btn{height:17px;line-height:17px;text-align:center;color:var(--white);font-size:7.8px}
.btn-green{background:var(--green)}
.btn-dark{background:var(--charcoal)}
.section-title{font-size:18px;font-weight:600;color:var(--ink)}
.slider-dot{width:14px;height:14px;border-radius:50%}
.product{width:134px;top:609px}
.product-photo{height:121px;border:1px solid #ddd;border-bottom:none;background:radial-gradient(circle at 50% 55%,#6b5a3e 0%,#8e7c63 22%,#e6e6e6 40%,#fafafa 70%)}
.product-badge{position:absolute;left:0;top:9px;width:33px;height:14px;font-size:8px;line-height:14px;text-align:center;color:var(--white)}
.product-info{height:56px;background:var(--card-info);text-align:center;padding-top:7px}
.product-name{font-size:8.5px;font-weight:600;color:var(--muted);line-height:12px}
.product-price{font-size:8.5px;font-weight:700;color:var(--ink);margin-top:6px}
.product-btn{height:23px;line-height:23px;text-align:center;color:var(--white);font-size:8.8px;font-weight:700}
.testimonials{left:0;top:851px;width:714px;height:186px;background:var(--panel)}
.quote-card{left:59px;top:908px;width:591px;height:72px;background:var(--white)}
.quote-text{left:120px;top:922px;width:470px;text-align:center;font-size:6.6px;line-height:10.5px;color:var(--muted)}
.quote-author{left:0;top:955px;width:714px;text-align:center;font-size:6.6px;font-weight:600;color:var(--ink)}
.quote-author span{color:#2e6aa8;font-weight:400}
.quote-mark{font-size:22px;font-weight:700;color:var(--charcoal);top:915px}
.footer{left:0;top:1037px;width:714px;height:163px;background:var(--green);color:var(--white)}
.footer-links{left:0;top:1048px;width:714px;text-align:center;font-size:8px;color:var(--white)}
.footer-links span{margin:0 8px}
.footer-h{font-size:9.5px;color:var(--white);top:1085px}
.footer-small{font-size:7.2px;line-height:10.5px;color:var(--white)}
.footer-divider{width:1px;height:64px;background:rgba(255,255,255,.25);top:1087px}
.subscribe-input{left:342px;top:1110px;width:127px;height:20px;background:var(--white);font-size:6.8px;color:#777;line-height:20px;padding-left:6px}
.subscribe-btn{left:469px;top:1110px;width:21px;height:20px;background:var(--orange)}
.social{left:572px;top:1110px;display:flex;gap:6px;font-size:7px;font-weight:600}
.social span{display:flex;align-items:center;gap:2px}
.social i{display:inline-block;width:5px;height:5px;background:var(--white)}
.footer-rule{left:58px;top:1168px;width:598px;height:1px;background:rgba(255,255,255,.2)}
.copyright{left:58px;top:1180px;font-size:7px;color:var(--white)}
.pay-badge{left:630px;top:1179px;width:28px;height:12px;background:var(--white);color:var(--green);font-size:5.5px;font-weight:700;text-align:center;line-height:12px}
</style>
</head>
<body>
<div class="abs top-rule"></div>

<header>
  <div class="abs brand">
    <div class="brand-mark"></div>
    <div class="brand-name">SILVERWELL TISANE HOUSE</div>
    <div class="brand-tag">• NATUROPATH, MEDICAL HERBALIST &amp; NUTRITIONIST •</div>
  </div>
  <div class="abs utility">My Account<span>|</span>Login<span>|</span>Support</div>
  <div class="abs utility-divider"></div>
  <div class="abs cart">Cart (empty)
    <svg width="20" height="16" viewBox="0 0 20 16" aria-hidden="true"><path d="M1 2h3l2 9h10l2-7H6" fill="none" stroke="#2d8a35" stroke-width="2"/><circle cx="8" cy="14" r="1.5" fill="#2d8a35"/><circle cx="15" cy="14" r="1.5" fill="#2d8a35"/></svg>
  </div>
  <nav class="abs nav">
    <a class="active" style="margin-right:19px">Home</a>
    <a style="margin-right:32px">About Us</a>
    <a style="margin-right:31px">Products</a>
    <a style="margin-right:30px">Gallery</a>
    <a style="margin-right:30px">Blog</a>
    <a>Contact Us</a>
  </nav>
</header>

<section>
  <div class="abs hero" role="img" aria-label="Glass cup of golden herbal tea with fresh mint leaves on a saucer"></div>
  <div class="abs hero-arrow" style="left:12px"><svg width="22" height="22"><path d="M13 6l-5 5 5 5" stroke="#fff" stroke-width="2" fill="none"/></svg></div>
  <div class="abs hero-arrow" style="left:677px"><svg width="22" height="22"><path d="M9 6l5 5-5 5" stroke="#fff" stroke-width="2" fill="none"/></svg></div>
  <div class="abs hero-caption">We blend organic tea recipes for medicinal purposes and for customer enjoyment</div>
</section>

<section>
  <h1 class="abs welcome-title">Welcome To Our Site</h1>
  <p class="abs welcome-text">Nullam vitae finibus purus. Nunc ornare, mauris sed tristique euismod, velit augue pharetra arcu, id suscipit nunc felis in arcu. Proin nunc tortor, pharetra eget augue vel, pellentesque varius velit. Vivamus ut arcu posuere, ornare neque vel, efficitur purus. Aenean vestibulum, eros ac euismod aliquam, dolor velit dapibus tortor, quis venenatis tortor tellus ut dolor. Vivamus orci neque, euismod a consequat vel, aliquam id orci. Fusce volutpat blandit erat, eget scelerisque magna luctus rutrum. Fusce non facilisis purus. Vivamus blandit luctus finibus.</p>
  <div class="abs btn btn-green" style="left:278px;top:513px;width:76px">Read More</div>
  <div class="abs btn btn-dark" style="left:360px;top:513px;width:77px">View Products</div>
</section>

<section>
  <h2 class="abs section-title" style="left:59px;top:570px">Our Products</h2>
  <div class="abs slider-dot" style="left:624px;top:574px;background:#222"><svg width="14" height="14"><path d="M8 4l-3 3 3 3" stroke="#fff" stroke-width="1.6" fill="none"/></svg></div>
  <div class="abs slider-dot" style="left:640px;top:574px;background:var(--green)"><svg width="14" height="14"><path d="M6 4l3 3-3 3" stroke="#fff" stroke-width="1.6" fill="none"/></svg></div>

  <div class="abs product" style="left:59px">
    <div class="product-photo" role="img" aria-label="Glass jar of loose leaf tea"></div>
    <div class="product-badge" style="background:var(--green)">100g</div>
    <div class="product-info"><div class="product-name">Lorem ipsum dolor sit ametco<br>nsectetur</div><div class="product-price">$538.00</div></div>
    <div class="product-btn" style="background:var(--green)">Add To Cart</div>
  </div>
  <div class="abs product" style="left:213px">
    <div class="product-photo" role="img" aria-label="Tall lidded glass jar of black tea"></div>
    <div class="product-badge" style="background:var(--charcoal)">100g</div>
    <div class="product-info"><div class="product-name">Lorem ipsum dolor sit ametco<br>nsectetur</div><div class="product-price">$538.00</div></div>
    <div class="product-btn" style="background:var(--charcoal)">Add To Cart</div>
  </div>
  <div class="abs product" style="left:367px">
    <div class="product-photo" role="img" aria-label="Open glass jar with dark loose tea"></div>
    <div class="product-badge" style="background:var(--charcoal)">100g</div>
    <div class="product-info"><div class="product-name">Lorem ipsum dolor sit ametco<br>nsectetur</div><div class="product-price">$538.00</div></div>
    <div class="product-btn" style="background:var(--charcoal)">Add To Cart</div>
  </div>
  <div class="abs product" style="left:521px">
    <div class="product-photo" role="img" aria-label="Cup of red tea beside a corked jar of tea leaves" style="background:radial-gradient(circle at 40% 60%,#8a2a1a 0%,#a8553f 18%,#e9e3dc 40%,#fafafa 70%)"></div>
    <div class="product-badge" style="background:var(--charcoal)">100g</div>
    <div class="product-info"><div class="product-name">Lorem ipsum dolor sit ametco<br>nsectetur</div><div class="product-price">$538.00</div></div>
    <div class="product-btn" style="background:var(--charcoal)">Add To Cart</div>
  </div>
</section>

<section>
  <div class="abs testimonials"></div>
  <h2 class="abs section-title" style="left:0;top:869px;width:714px;text-align:center">Client Testimonials</h2>
  <div class="abs quote-card"></div>
  <div class="abs quote-mark" style="left:72px">“</div>
  <div class="abs quote-mark" style="left:622px">”</div>
  <p class="abs quote-text">Etiam in tincidunt arcu, at tempor magna. Maecenas ut odio nunc. Fusce aliquet sem et sollicitudin tincidunt.<br>Aliquam convallis vitae metus ut luctus. Nulla vestibulum consequat sem, nec molestie tellus consectetur nec. In molestie sapien a convallis egestas.</p>
  <div class="abs quote-author">- Jane Marlow, <span>developer</span></div>
  <svg class="abs" style="left:339px;top:1011px" width="30" height="6" aria-hidden="true"><circle cx="3" cy="3" r="2.5" fill="#2d8a35"/><circle cx="15" cy="3" r="2.5" fill="#ddd"/><circle cx="27" cy="3" r="2.5" fill="#ddd"/></svg>
</section>

<footer>
  <div class="abs footer"></div>
  <div class="abs footer-links">About us<span>|</span>FAQ<span>|</span>Product</div>
  <div class="abs footer-h" style="left:59px">Contact us</div>
  <div class="abs footer-small" style="left:59px;top:1108px">Fernleaf Trading Co.<br>48 Meadow Lane Greyford, HJ 07120<br>United States</div>
  <div class="abs footer-small" style="left:197px;top:1108px">+1 (555) 014 - 2270<br>support@silverwell.example</div>
  <div class="abs footer-divider" style="left:311px"></div>
  <div class="abs footer-h" style="left:340px">Subscribe here</div>
  <div class="abs subscribe-input">Enter your email</div>
  <div class="abs subscribe-btn"><svg width="21" height="20"><path d="M9 6l4 4-4 4" stroke="#fff" stroke-width="1.6" fill="none"/></svg></div>
  <div class="abs footer-divider" style="left:535px"></div>
  <div class="abs footer-h" style="left:584px">Social Media</div>
  <div class="abs social"><span><i></i>Leafbook</span><span><i></i>Tumbleaf</span><span><i></i>Petalgram</span></div>
  <div class="abs footer-rule"></div>
  <div class="abs copyright">Copyrights 2015 © silverwell. All rights Reserved</div>
  <div class="abs pay-badge">Quorvex</div>
</footer>
</body>
</html>
```